Verpackungen für Duschbrausen
Zielgruppe
Wir verkaufen verschiedene Produkte über E-Commerce Plattformen. Zielgruppe sind in diesem Fall alle die eine neue Duschbrause benötigen.
Aufgabenstellung
Liebe Grafikerinnen und Grafiker,
wir werden eine neue Produktlinie von Duschbrausen auf den Markt bringen und benötigen dafür eine frische, ansprechende Umverpackung. Eure Kreativität und Expertise sind gefragt, um eine Verpackung zu gestalten, die sowohl für verschiedene Duschbrausenmodelle geeignet ist als auch neutral und ansprechend wirkt.
Unser Ziel ist es, eine Verpackung zu kreieren, die sich von anderen abhebt, aber dennoch einen gewissen Neutralitätsgrad beibehält. Die Verpackung sollte modern, professionell und ansprechend gestaltet sein, um die Aufmerksamkeit der Kunden zu gewinnen.
Im Anhang findet ihr Beispiele von anderen Firmen (Zip Datei Verpackung Mitbewerber), wie sie ihre Duschbrausen verpacken. Diese dienen lediglich zur Inspiration und sollen euch einen Einblick in den aktuellen Markt geben. Wir ermutigen euch jedoch dazu, eure eigenen kreativen Ideen einzubringen und eine einzigartige Umverpackung zu entwerfen.
Bitte beachtet bei euren Entwürfen folgende Punkte:
Neutralität: Die Verpackung sollte für verschiedene Duschbrausenmodelle geeignet sein.
Modernität: Ein zeitgemäßes Design
Ansprechendes Layout: Klare Strukturen und gut lesbare Informationen.
Wir sind sehr gespannt auf eure Vorschläge :-)
Bei Fragen oder Unklarheiten stehe ich euch gerne zur Verfügung. Vielen Dank im Voraus für eure kreative Arbeit!
Mit freundlichen Grüßen,
Bertold

```html
<!DOCTYPE html>
<html lang="de">
<head>
<meta charset="utf-8">
<title>MERIO – Faltschachtel Duschkopf</title>
<link href="https://fonts.googleapis.com/css2?family=Open+Sans:wght@300;400;600&display=swap" rel="stylesheet">
<style>
  :root {
    --ink: #000000;
    --dieline: #1f8a4c;
    --accent: #5bc2de;
    --label-bg: #f3f1f2;
    --band-bg: #333333;
    --white: #ffffff;
    --splash-dark: #0b0b0b;
    --splash-mid: #2a2a2a;
    --chrome-light: #e9ecee;
    --chrome-dark: #9ea4a8;
  }
  html, body {
    margin: 0;
    padding: 0;
    width: 1200px;
    height: 2407px;
    overflow: hidden;
    background: var(--ink);
  }
  .dieline-sheet {
    position: relative;
    width: 1200px;
    height: 2407px;
    font-family: "Open Sans", Arial, sans-serif;
  }
  .artwork {
    position: absolute;
    inset: 0;
  }
  .brand-label {
    position: absolute;
    left: 138px;
    top: 650px;
    width: 450px;
    height: 144px;
    background: var(--label-bg);
    display: flex;
    align-items: center;
    justify-content: center;
  }
  .brand-name {
    font-family: "Open Sans", Arial, sans-serif;
    font-weight: 300;
    font-size: 82px;
    letter-spacing: 38px;
    margin-right: -38px;
    color: var(--accent);
    line-height: 1;
  }
  .claim-band {
    position: absolute;
    left: 62px;
    top: 1886px;
    width: 658px;
    height: 217px;
    background: var(--band-bg);
    color: var(--white);
  }
  .claim-kicker {
    position: absolute;
    left: 109px;
    top: 24px;
    font-size: 35px;
    font-weight: 400;
    letter-spacing: 0.5px;
    line-height: 1;
  }
  .claim-title {
    position: absolute;
    left: 107px;
    top: 60px;
    font-size: 57px;
    font-weight: 400;
    line-height: 1;
  }
  .claim-copy {
    position: absolute;
    left: 108px;
    top: 132px;
    font-size: 28px;
    line-height: 33px;
  }
  .eco-drop {
    position: absolute;
    left: 454px;
    top: 20px;
    width: 92px;
    height: 132px;
  }
</style>
</head>
<body>
<div class="dieline-sheet">

  <svg class="artwork" width="1200" height="2407" viewBox="0 0 1200 2407" xmlns="http://www.w3.org/2000/svg">
    <defs>
      <linearGradient id="splash-tone" x1="0" y1="0" x2="1" y2="1">
        <stop offset="0" stop-color="var(--splash-dark)"/>
        <stop offset="0.5" stop-color="var(--splash-mid)"/>
        <stop offset="1" stop-color="var(--splash-dark)"/>
      </linearGradient>
      <linearGradient id="chrome-tone" x1="0" y1="0" x2="1" y2="0">
        <stop offset="0" stop-color="var(--chrome-light)"/>
        <stop offset="0.6" stop-color="#d3d7da"/>
        <stop offset="1" stop-color="var(--chrome-dark)"/>
      </linearGradient>
    </defs>

    <!-- water splash background across front and side panel -->
    <rect class="splash-photo" x="62" y="479" width="1138" height="1641" fill="url(#splash-tone)"
          role="img" aria-label="Foto: Wasserspritzer auf schwarzem Hintergrund"/>

    <!-- hand shower product shot -->
    <rect class="product-photo" x="393" y="650" width="546" height="1444" rx="250" fill="url(#chrome-tone)"
          role="img" aria-label="Produktfoto: verchromte Handbrause mit runder Strahlscheibe"/>

    <!-- model name on front and side panel -->
    <text class="model-name" transform="translate(574 1766) rotate(-90)"
          font-family="Open Sans, Arial, sans-serif" font-weight="600" font-size="92"
          fill="var(--accent)" textLength="512" lengthAdjust="spacingAndGlyphs">fluo KR-305</text>
    <text class="model-name" transform="translate(1061 1766) rotate(-90)"
          font-family="Open Sans, Arial, sans-serif" font-weight="600" font-size="92"
          fill="var(--accent)" textLength="512" lengthAdjust="spacingAndGlyphs">fluo KR-305</text>

    <!-- die cut and fold lines -->
    <g class="dieline" fill="none" stroke="var(--dieline)" stroke-width="2.5">
      <!-- top tuck flap and hanger panels -->
      <polyline points="116,479 116,54 123,45 853,45 859,54 859,479"/>
      <line x1="116" y1="140" x2="859" y2="140"/>
      <line x1="116" y1="308" x2="859" y2="308"/>
      <line x1="116" y1="479" x2="1200" y2="479"/>
      <!-- front panel -->
      <rect x="116" y="479" width="743" height="1641"/>
      <!-- side dust flap top -->
      <polyline points="859,479 896,252 1162,252 1200,479"/>
      <!-- side panel -->
      <line x1="1200" y1="479" x2="1200" y2="2120"/>
      <line x1="859" y1="2120" x2="1200" y2="2120"/>
      <!-- glue flap -->
      <polyline points="116,479 23,503 23,2094 116,2120"/>
      <!-- bottom flap front -->
      <polyline points="116,2120 301,2293 301,2383 675,2383 675,2293 859,2120"/>
      <!-- bottom flap side -->
      <polyline points="859,2120 859,2383 1029,2383 1029,2293 1200,2120"/>
    </g>

    <!-- hanger holes -->
    <g class="hanger-hole" fill="var(--white)" stroke="var(--dieline)" stroke-width="2.5">
      <path d="M427,213 H574 A19,19 0 0 1 574,251 H529 A22,22 0 0 1 483,251 H427 A19,19 0 0 1 427,213 Z"/>
      <path d="M427,405 H574 A19,19 0 0 0 574,367 H529 A22,22 0 0 0 483,367 H427 A19,19 0 0 0 427,405 Z"/>
    </g>
  </svg>

  <div class="brand-label">
    <span class="brand-name">MERIO</span>
  </div>

  <div class="claim-band">
    <div class="claim-kicker">WASSERSPARENDER</div>
    <div class="claim-title">DUSCHKOPF</div>
    <div class="claim-copy">Lorem ipsum dolor sit<br>amet, consectetur adipiscing</div>
    <svg class="eco-drop" viewBox="0 0 92 132" role="img" aria-label="Symbol: Wassertropfen mit Pflanzenkeim">
      <defs>
        <linearGradient id="drop-tone" x1="0" y1="0" x2="0" y2="1">
          <stop offset="0" stop-color="#8fd6f0"/>
          <stop offset="1" stop-color="#1478c2"/>
        </linearGradient>
      </defs>
      <path d="M46,2 C58,40 90,62 90,90 A44,40 0 0 1 2,90 C2,62 34,40 46,2 Z" fill="url(#drop-tone)"/>
    </svg>
  </div>

</div>
</body>
</html>
```